Visitenkarten-Design für private Praxis für Sprachtherapie
Zielgruppe
Private Praxis für Sprachtherapie (Logopädie)
Aufgabenstellung
Siehe PDF der Anlage.

```html
<!DOCTYPE html>
<html lang="de">
<head>
<meta charset="utf-8">
<title>Visitenkarte Praxis für Sprachtherapie</title>
<link href="https://fonts.googleapis.com/css2?family=Fira+Sans+Condensed:wght@400;500;600&display=swap" rel="stylesheet">
<style>
:root{
  --navy:#13215a;
  --paper:#e9f5fc;
  --mist:#d4ebf8;
  --sky:#a3daf2;
  --steel:#5b7ab8;
  --white:#ffffff;
  --stage:#f6f9fb;
}
*{margin:0;padding:0;box-sizing:border-box}
html,body{width:1200px;height:1200px;overflow:hidden}
body{background:linear-gradient(160deg,#fbfcfd,#eef3f7);font-family:"Fira Sans Condensed",sans-serif;color:var(--navy);position:relative}
.card{position:absolute;top:266px;width:432px;height:667px;background:var(--paper);overflow:hidden;box-shadow:0 2px 8px rgba(0,0,0,.18)}
.card--front{left:145px}
.card--back{left:623px}
.wave{position:absolute;left:0;width:432px}
.motif{position:absolute;border-radius:40% 50% 45% 40%;background:radial-gradient(ellipse at center,var(--mist) 0%,rgba(212,235,248,.6) 55%,rgba(233,245,252,0) 75%)}
.brand{position:absolute;left:0;width:432px;top:30px;height:175px}
.brand__ring{position:absolute;left:131px;top:0;width:172px;height:172px;border:2px solid var(--navy);border-radius:50%}
.brand__name{position:absolute;left:0;width:432px;top:72px;text-align:center;font-size:22px;font-weight:600;color:var(--navy)}
.front__title{position:absolute;left:0;width:432px;top:250px;text-align:center;font-weight:600;font-size:33px;line-height:40px}
.front__address{position:absolute;left:0;width:432px;top:339px;text-align:center;font-size:26px;line-height:33px}
.contact{position:absolute;left:0;width:432px;top:470px;text-align:center;font-size:26px;line-height:39px}
.contact__line{display:flex;align-items:center;justify-content:center;gap:8px}
.contact__icon{width:20px;height:20px;fill:var(--steel)}
.field__label{position:absolute;left:26px;font-size:19px;line-height:19px;color:#111}
.field__box{position:absolute;left:152px;width:260px;height:45px;background:var(--white)}
.appt__title{position:absolute;left:0;width:432px;top:287px;text-align:center;color:var(--white);font-weight:600;font-size:28px}
.appt__head{position:absolute;top:327px;height:41px;background:var(--steel);color:var(--white);font-size:24px;display:flex;align-items:center;justify-content:center}
.appt__cell{position:absolute;height:46px;background:var(--white)}
</style>
</head>
<body>

<section class="card card--front">
  <div class="motif" role="img" aria-label="Dezente Illustration: Profil eines Kopfes mit Schallwellen" style="left:-20px;top:170px;width:420px;height:420px"></div>

  <div class="brand">
    <div class="brand__ring"></div>
    <div class="brand__name">Marlene Kessing</div>
  </div>

  <h1 class="front__title">Praxis für Sprachtherapie<br>Marlene Kessing</h1>
  <p class="front__address">Lindenweg 14<br>48151 Brakenfeld</p>

  <div class="contact">
    <div class="contact__line">
      <svg class="contact__icon" viewBox="0 0 24 24"><path d="M6.6 10.8a15 15 0 0 0 6.6 6.6l2.2-2.2c.3-.3.7-.4 1-.2 1.1.4 2.3.6 3.6.6.6 0 1 .4 1 1V20c0 .6-.4 1-1 1A17 17 0 0 1 3 4c0-.6.4-1 1-1h3.5c.6 0 1 .4 1 1 0 1.3.2 2.5.6 3.6.1.3 0 .7-.2 1z"/></svg>
      <span>05231 448192</span>
    </div>
    <div class="contact__line">
      <svg class="contact__icon" viewBox="0 0 24 24"><path d="M2 5h20v14H2z" opacity=".9"/><path d="M2 5l10 7 10-7" fill="none" stroke="#e9f5fc" stroke-width="1.6"/></svg>
      <span>info@sprachpraxis-kessing.de</span>
    </div>
    <div class="contact__line">
      <svg class="contact__icon" viewBox="0 0 24 24"><circle cx="12" cy="12" r="9" fill="none" stroke="#5b7ab8" stroke-width="2"/><path d="M3 12h18M12 3c3 3 3 15 0 18M12 3c-3 3-3 15 0 18" fill="none" stroke="#5b7ab8" stroke-width="1.6"/></svg>
      <span>sprachpraxis-kessing.de</span>
    </div>
  </div>

  <svg class="wave" style="top:570px;height:97px" viewBox="0 0 432 97" preserveAspectRatio="none">
    <path d="M0 35 C90 65 190 70 290 40 C360 20 400 10 432 10 V97 H0Z" fill="var(--sky)"/>
    <path d="M0 45 C120 75 200 68 290 40 C360 20 400 12 432 12 V97 H0Z" fill="var(--steel)"/>
    <path d="M0 53 C110 82 210 80 300 52 C370 30 405 22 432 26 V97 H0Z" fill="var(--navy)"/>
  </svg>
</section>

<section class="card card--back">
  <div class="motif" role="img" aria-label="Dezente Illustration: Profil eines Kopfes mit Schallwellen" style="left:-30px;top:90px;width:170px;height:160px"></div>

  <span class="field__label" style="top:30px">Vor- und<br>Nachname</span>
  <div class="field__box" style="top:24px"></div>
  <span class="field__label" style="top:93px">Funktion</span>
  <div class="field__box" style="top:81px"></div>
  <span class="field__label" style="top:147px">Telefonnummer</span>
  <div class="field__box" style="top:135px"></div>
  <span class="field__label" style="top:202px">E-Mail-Adresse</span>
  <div class="field__box" style="top:190px"></div>

  <svg class="wave" style="top:210px;height:457px" viewBox="0 0 432 457" preserveAspectRatio="none">
    <path d="M0 30 C100 70 220 75 330 40 C380 25 410 22 432 24 V457 H0Z" fill="var(--sky)"/>
    <path d="M0 52 C110 90 220 90 320 60 C370 45 405 37 432 40 V457 H0Z" fill="var(--navy)"/>
  </svg>

  <h2 class="appt__title">Ihr nächsten Termin</h2>
  <div class="appt__head" style="left:19px;width:137px">Wochentag</div>
  <div class="appt__head" style="left:168px;width:96px">Datum</div>
  <div class="appt__head" style="left:276px;width:136px">Uhrzeit</div>

  <div class="appt__cell" style="left:19px;width:137px;top:378px"></div>
  <div class="appt__cell" style="left:168px;width:96px;top:378px"></div>
  <div class="appt__cell" style="left:276px;width:136px;top:378px"></div>
  <div class="appt__cell" style="left:19px;width:137px;top:433px"></div>
  <div class="appt__cell" style="left:168px;width:96px;top:433px"></div>
  <div class="appt__cell" style="left:276px;width:136px;top:433px"></div>
  <div class="appt__cell" style="left:19px;width:137px;top:489px"></div>
  <div class="appt__cell" style="left:168px;width:96px;top:489px"></div>
  <div class="appt__cell" style="left:276px;width:136px;top:489px"></div>
  <div class="appt__cell" style="left:19px;width:137px;top:544px"></div>
  <div class="appt__cell" style="left:168px;width:96px;top:544px"></div>
  <div class="appt__cell" style="left:276px;width:136px;top:544px"></div>
  <div class="appt__cell" style="left:19px;width:137px;top:599px"></div>
  <div class="appt__cell" style="left:168px;width:96px;top:599px"></div>
  <div class="appt__cell" style="left:276px;width:136px;top:599px"></div>
</section>

</body>
</html>
```